Meridian Groundworks
Project: Construction Stationery
Construction Stationery - Construction
Construction Stationery
Professional
Eng. Samir Qutub
Construction Manager
P.O.Box: 4706 Jeddah 23857 Palm Orchard Street Saudi Arabia Phone: +966 12 4870391 info@meridiangroundworks.example
info@meridiangroundworks.example
www.meridiangroundworks.example
Please don't submit business card solo, submit the following at once:- 1. Business card 2. Letterhead A 3. Letterhead B 4. Envelope 5. Notepad 6. Folder
Design
kelvorunt kelvorunt
Please don't submit business card solo, I don't need all stationery i need only what's mentioned in additional comments section in the brief. Please check attached logo.

```html
<!DOCTYPE html>
<html lang="en">
<head>
<meta charset="utf-8">
<title>Meridian Groundworks – Stationery</title>
<link href="https://fonts.googleapis.com/css2?family=Montserrat:wght@800&family=Open+Sans:wght@400;600&display=swap" rel="stylesheet">
<style>
:root{
  --bg:#e9eaec;
  --paper:#ffffff;
  --navy:#1f2f7a;
  --blue:#2f5fd0;
  --blue-light:#4f86e8;
  --orange:#f0922a;
  --ink:#4a4f5a;
  --muted:#8a8f99;
}
*{box-sizing:border-box;margin:0;padding:0}
html,body{width:1200px;height:936px;overflow:hidden;background:var(--bg)}
body{position:relative;font-family:"Open Sans",Arial,sans-serif;color:var(--ink)}
.sheet{position:absolute;background:var(--paper);overflow:hidden}

.brand{display:flex;align-items:center;gap:6px}
.brand-dot{border-radius:50%;background:var(--blue);flex:none}
.brand-name{font-family:"Montserrat",Arial,sans-serif;font-weight:800;color:var(--navy);line-height:1.05;text-transform:uppercase;letter-spacing:.04em}

.web-bar{position:absolute;left:0;right:0;bottom:0;background:linear-gradient(90deg,var(--navy),var(--blue-light));color:#fff;text-align:center;letter-spacing:.18em}

/* letterhead */
.letterhead{left:183px;top:33px;width:390px;height:578px}
.letterhead .edge{position:absolute;left:0;top:18px;width:8px;height:60px;background:linear-gradient(180deg,var(--blue-light),var(--navy));border-radius:0 8px 8px 0}
.letterhead .brand{position:absolute;left:24px;top:28px}
.letterhead .brand-dot{width:22px;height:22px}
.letterhead .brand-name{font-size:10px}
.contact-block{position:absolute;right:20px;top:26px;text-align:right;font-size:5.5px;line-height:9px;color:var(--muted)}
.contact-block span{display:inline-block;width:4px;height:4px;background:var(--blue);border-radius:50%;margin-left:4px;vertical-align:middle}
.letter{position:absolute;left:24px;top:122px;width:300px;font-size:5.6px;line-height:8.6px}
.letter p{margin-bottom:9px}
.signature{width:46px;height:16px;background:linear-gradient(90deg,#d8dbe2,#eef0f4);margin:4px 0 4px}
.letterhead .web-bar{height:14px;font-size:6px;line-height:14px}

/* folder */
.folder{left:634px;top:33px;width:531px;height:584px}
.folder .tab{position:absolute;left:0;top:297px;width:22px;height:114px;background:linear-gradient(180deg,var(--blue-light),var(--navy));border-radius:0 14px 14px 0}
.folder .brand{position:absolute;left:0;right:0;top:238px;flex-direction:column;gap:10px}
.folder .brand-dot{width:56px;height:56px}
.folder .brand-name{font-size:30px;text-align:center}
.folder .web-bar{height:26px;font-size:8px;line-height:26px}

/* business cards */
.card{left:43px;width:203px;height:108px;border-radius:8px}
.card-front{top:665px}
.card-front .brand{position:absolute;right:12px;top:16px;gap:4px}
.card-front .brand-dot{width:12px;height:12px}
.card-front .brand-name{font-size:6.5px}
.card-front .contacts{position:absolute;left:12px;top:48px;font-size:4.6px;line-height:8px;color:var(--muted)}
.card-front .contacts b{font-weight:600;color:var(--navy)}
.card-front .stripe{position:absolute;left:0;right:0;bottom:0;height:6px;background:linear-gradient(90deg,var(--navy),var(--blue-light))}
.card-back{top:781px}
.card-back .brand{position:absolute;left:40px;top:40px;gap:5px}
.card-back .brand-dot{width:16px;height:16px}
.card-back .brand-name{font-size:8px}

/* envelopes */
.envelope{top:670px;width:434px;height:213px}
.envelope-front{left:264px}
.envelope-front .brand{position:absolute;left:16px;top:18px;gap:6px}
.envelope-front .brand-dot{width:24px;height:24px}
.envelope-front .brand-name{font-size:13px}
.envelope-front .stripe{position:absolute;left:0;width:300px;bottom:22px;height:6px;background:linear-gradient(90deg,var(--navy),var(--blue-light))}
.envelope-back{left:738px}
.envelope-back svg{position:absolute;left:0;top:0}
.envelope-back .flap-web{position:absolute;left:0;right:0;top:34px;text-align:center;color:#fff;font-size:8px;letter-spacing:.18em}
</style>
</head>
<body>

<section class="sheet letterhead">
  <div class="edge"></div>
  <div class="brand"><span class="brand-dot"></span><span class="brand-name">Meridian<br>Groundworks</span></div>
  <div class="contact-block">
    <div>+966 12 4870391<span></span></div>
    <div>info@meridiangroundworks.example<span></span></div>
    <div>www.meridiangroundworks.example<span></span></div>
    <div>P.O.Box: 4706 Jeddah 23857<span></span></div>
    <div>Palm Orchard Street, Saudi Arabia<span></span></div>
  </div>
  <div class="letter">
    <p>2 June 2024</p>
    <p>Dear Client,<br>Subject: Groundwork Schedule</p>
    <p>We are pleased to confirm that our team has completed the soil survey and excavation plan for your project. The attached schedule outlines each stage of the groundwork, from site clearing to the final compaction test, along with the crew and equipment assigned to every phase.</p>
    <p>Please review the proposed dates and let us know if any changes are needed. Our engineers are available to meet on site at your convenience.</p>
    <p>We look forward to working with you and to delivering a safe, solid foundation on time and within budget. Thank you for your continued trust in our work.</p>
    <p>Sincerely,</p>
    <div class="signature" role="img" aria-label="Handwritten signature"></div>
    <p>Eng. Samir Qutub<br>Construction Manager</p>
  </div>
  <div class="web-bar">www.meridiangroundworks.example</div>
</section>

<section class="sheet folder">
  <div class="tab"></div>
  <div class="brand"><span class="brand-dot"></span><span class="brand-name">Meridian<br>Groundworks</span></div>
  <div class="web-bar">www.meridiangroundworks.example</div>
</section>

<section class="sheet card card-front">
  <div class="brand"><span class="brand-dot"></span><span class="brand-name">Meridian<br>Groundworks</span></div>
  <div class="contacts">
    <div><b>Eng. Samir Qutub</b> · Construction Manager</div>
    <div>+966 12 4870391</div>
    <div>info@meridiangroundworks.example</div>
    <div>P.O.Box: 4706 Jeddah 23857</div>
  </div>
  <div class="stripe"></div>
</section>

<section class="sheet card card-back">
  <div class="brand"><span class="brand-dot"></span><span class="brand-name">Meridian<br>Groundworks</span></div>
</section>

<section class="sheet envelope envelope-front">
  <div class="brand"><span class="brand-dot"></span><span class="brand-name">Meridian<br>Groundworks</span></div>
  <div class="stripe"></div>
</section>

<section class="sheet envelope envelope-back">
  <svg width="434" height="213" viewBox="0 0 434 213">
    <defs>
      <linearGradient id="flapFill" x1="0" x2="1" y1="0" y2="0">
        <stop offset="0" stop-color="#1f2f7a"/>
        <stop offset="1" stop-color="#4f86e8"/>
      </linearGradient>
    </defs>
    <path d="M0 0H434V78Q217 112 0 78Z" fill="url(#flapFill)"/>
  </svg>
  <div class="flap-web">www.meridiangroundworks.example</div>
</section>

</body>
</html>
```